PLUMBER,DRAINER,GASFITTER/LPG
blocked drains
new installations
maintenance
stormwater
gutters
all plumbing requirements
no job to small
HONEST RELIABLE FAIR
HI I'm after a professional flyer something that grabs the eye with all the above information in point form, i want to offer free quotes aswell.!
i want my email on there .... pipewarden-example.com
also i want have ...... 24 hour emergency service on there in red and
my lic no 842091k.
and I'm on Facebook under TIDELINE PLUMBING aswell.
any other information needed its on my website as above
i like the colours black and blue as in photo uploaded .
but very open to anything that you think could be good,

```html
<!DOCTYPE html>
<html lang="en">
<head>
<meta charset="utf-8">
<title>Tideline Plumbing Flyer</title>
<link href="https://fonts.googleapis.com/css2?family=Fira+Sans+Condensed:wght@300;500;600&family=Fira+Sans+Extra+Condensed:wght@500&family=Arimo&family=Montserrat:wght@500&display=swap" rel="stylesheet">
<style>
  :root {
    --backdrop: #bcbcbb;
    --paper: #ffffff;
    --brand-blue: #29a8e0;
    --brand-blue-dark: #17759c;
    --alert-red: #e2232a;
    --ink: #111111;
    --placeholder-light: #f1f3f5;
    --placeholder-mid: #d9dde2;
  }
  * { box-sizing: border-box; margin: 0; padding: 0; }
  html, body { width: 1200px; height: 1200px; overflow: hidden; }
  body { background: var(--backdrop); position: relative; }

  .flyer {
    position: absolute; left: 30px; top: 197px;
    width: 1141px; height: 806px;
    background: var(--paper); overflow: hidden;
  }
  .flyer-shapes { position: absolute; inset: 0; }

  .brand-name {
    position: absolute; left: 41px; top: 102px; width: 229px;
    text-align: center; color: var(--brand-blue); white-space: nowrap;
    font: 500 19px/1 "Montserrat", sans-serif; letter-spacing: 0.3px;
  }
  .licence {
    position: absolute; left: 41px; top: 138px; width: 229px;
    text-align: center; color: var(--brand-blue);
    font: 300 19px/1 "Fira Sans Condensed", sans-serif;
  }

  .trade-banner {
    position: absolute; left: 370px; top: 60px; width: 694px;
    text-align: center; white-space: nowrap;
    color: var(--paper);
    font: 500 52px/1 "Fira Sans Extra Condensed", sans-serif;
    letter-spacing: -0.5px;
  }

  .mascot-area {
    position: absolute; left: 142px; top: 231px; width: 248px; height: 360px;
    border-radius: 40px;
    background: radial-gradient(ellipse at 50% 40%, var(--placeholder-light), var(--placeholder-mid));
  }

  .service-list { position: absolute; left: 528px; top: 164px; list-style: none; }
  .service-list li {
    display: flex; align-items: center; height: 60px; white-space: nowrap;
    color: var(--ink); font: 500 47px/1 "Fira Sans Condensed", sans-serif;
  }
  .service-list .tick { width: 38px; height: 38px; margin-right: 24px; flex: none; }

  .emergency {
    position: absolute; left: 54px; top: 606px;
    display: flex; align-items: center; gap: 12px; white-space: nowrap;
    color: var(--alert-red); font: 600 26px/1 "Fira Sans Condensed", sans-serif;
  }
  .emergency svg { width: 52px; height: 52px; }

  .free-quotes {
    position: absolute; left: 106px; top: 682px; width: 322px; height: 66px;
    border: 2px dashed var(--alert-red); white-space: nowrap;
    display: flex; align-items: center; justify-content: center;
    color: var(--alert-red); font: 300 31px/1 "Fira Sans Condensed", sans-serif;
  }

  .contact-list { position: absolute; left: 650px; top: 673px; list-style: none; }
  .contact-list li {
    display: flex; align-items: center; gap: 14px; height: 43px; white-space: nowrap;
    color: var(--paper); font: 23px/1 "Arimo", sans-serif;
  }
  .contact-list svg { width: 28px; height: 28px; flex: none; }
</style>
</head>
<body>
<main class="flyer">
  <svg class="flyer-shapes" viewBox="0 0 1141 806" aria-hidden="true">
    <defs>
      <filter id="soft-shadow" x="-20%" y="-20%" width="140%" height="140%">
        <feDropShadow dx="0" dy="3" stdDeviation="5" flood-opacity="0.25"/>
      </filter>
    </defs>
    <polygon points="41,0 270,0 270,154 161,184 41,154" fill="var(--paper)" filter="url(#soft-shadow)"/>
    <line x1="60" y1="129" x2="251" y2="129" stroke="var(--brand-blue)" stroke-width="1.5"/>
    <polygon points="1066,130 1114,130 1078,174" fill="var(--brand-blue-dark)"/>
    <polygon points="326,44 1066,44 1114,130 374,130" fill="var(--brand-blue)" filter="url(#soft-shadow)"/>
    <path d="M0,686 C120,706 200,716 330,706 C520,690 700,650 854,654 C980,658 1080,680 1141,694 L1141,806 L0,806 Z" fill="var(--brand-blue)"/>
  </svg>

  <div class="brand-name">TIDELINE PLUMBING</div>
  <div class="licence">lic no 842091k</div>

  <h1 class="trade-banner">PLUMBER,DRAINER,GASFITTER/LPG</h1>

  <div class="mascot-area" role="img" aria-label="Illustration of a plumber figure in a hard hat and goggles holding a large wrench and giving a thumbs up"></div>

  <ul class="service-list">
    <li><svg class="tick" viewBox="0 0 38 38"><path d="M3,20 L14,33 L35,3" fill="none" stroke="var(--brand-blue)" stroke-width="3"/></svg>Blocked drains</li>
    <li><svg class="tick" viewBox="0 0 38 38"><path d="M3,20 L14,33 L35,3" fill="none" stroke="var(--brand-blue)" stroke-width="3"/></svg>New installations</li>
    <li><svg class="tick" viewBox="0 0 38 38"><path d="M3,20 L14,33 L35,3" fill="none" stroke="var(--brand-blue)" stroke-width="3"/></svg>Maintenance</li>
    <li><svg class="tick" viewBox="0 0 38 38"><path d="M3,20 L14,33 L35,3" fill="none" stroke="var(--brand-blue)" stroke-width="3"/></svg>Stormwater</li>
    <li><svg class="tick" viewBox="0 0 38 38"><path d="M3,20 L14,33 L35,3" fill="none" stroke="var(--brand-blue)" stroke-width="3"/></svg>Gutters</li>
    <li><svg class="tick" viewBox="0 0 38 38"><path d="M3,20 L14,33 L35,3" fill="none" stroke="var(--brand-blue)" stroke-width="3"/></svg>All plumbing requirements</li>
    <li><svg class="tick" viewBox="0 0 38 38"><path d="M3,20 L14,33 L35,3" fill="none" stroke="var(--brand-blue)" stroke-width="3"/></svg>No job to small</li>
    <li><svg class="tick" viewBox="0 0 38 38"><path d="M3,20 L14,33 L35,3" fill="none" stroke="var(--brand-blue)" stroke-width="3"/></svg>HONEST RELIABLE FAIR</li>
  </ul>

  <div class="emergency">
    <svg viewBox="0 0 52 52" aria-hidden="true">
      <path d="M8,22 A19,19 0 1 0 26,7" fill="none" stroke="var(--alert-red)" stroke-width="4" stroke-dasharray="60 4 3 4 3 4 3 4 3 4 3"/>
      <polygon points="2,22 14,22 8,12" fill="var(--alert-red)"/>
      <text x="26" y="33" text-anchor="middle" font-family="Fira Sans Condensed, sans-serif" font-weight="600" font-size="17" fill="var(--alert-red)">24</text>
    </svg>
    <span>24 HOUR EMERGENCY SERVICE</span>
  </div>

  <div class="free-quotes">OFFER FREE QUOTES</div>

  <ul class="contact-list">
    <li>
      <svg viewBox="0 0 28 28" aria-hidden="true"><circle cx="14" cy="14" r="14" fill="var(--paper)"/><path d="M9,7 L12,7 L13,11 L11,13 C12,15.5 13.5,17 15.5,17.5 L17.5,15.5 L21,16.5 L21,19.5 C21,20.5 20,21 19,21 C13,20.5 7.5,15 7,9 C7,8 8,7 9,7 Z" fill="var(--brand-blue)"/></svg>
      <span>office@pipewarden-example.com</span>
    </li>
    <li>
      <svg viewBox="0 0 28 28" aria-hidden="true"><circle cx="14" cy="14" r="14" fill="var(--paper)"/><g fill="none" stroke="var(--brand-blue)" stroke-width="1.4"><circle cx="14" cy="14" r="7"/><ellipse cx="14" cy="14" rx="3" ry="7"/><line x1="7" y1="14" x2="21" y2="14"/><line x1="8" y1="10.5" x2="20" y2="10.5"/><line x1="8" y1="17.5" x2="20" y2="17.5"/></g></svg>
      <span>www.pipewarden-example.com.au</span>
    </li>
    <li>
      <svg viewBox="0 0 28 28" aria-hidden="true"><circle cx="14" cy="14" r="14" fill="var(--paper)"/></svg>
      <span>TIDELINE PLUMBING</span>
    </li>
  </ul>
</main>
</body>
</html>
```